Product flyer with pricing

We manufacture iconic and luxury vending trailers. for our first trailer we need a flyer created to give to prospective clients with base pricing. I am uploading an example along with graphic files.

```html
<!DOCTYPE html>
<html lang="en">
<head>
<meta charset="UTF-8">
<title>Cottage Crest Mini – Luxury Mobile Vending House</title>
<link rel="stylesheet" href="https://fonts.googleapis.com/css2?family=Barlow:wght@400;600;700&family=Barlow+Condensed:wght@600;700&display=swap">
<style>
  :root {
    --navy: #17335c;
    --ink: #1e3350;
    --banner: #2e5a8a;
    --band: #2480e0;
    --paper: #f1f2f4;
    --white: #ffffff;
  }
  html, body { margin: 0; padding: 0; overflow: hidden; }
  .flyer {
    position: relative;
    width: 927px;
    height: 1200px;
    overflow: hidden;
    background: var(--paper);
    font-family: "Barlow", sans-serif;
    color: var(--ink);
  }
  .flyer-art { position: absolute; inset: 0; }
  .title-banner {
    position: absolute;
    left: 0; top: 337px;
    width: 484px; height: 130px;
    text-align: center;
    color: var(--white);
    font-family: "Barlow Condensed", sans-serif;
    font-weight: 600;
    font-size: 31px;
    line-height: 36px;
    padding-top: 13px;
    box-sizing: border-box;
    padding-right: 0;
    width: 484px;
  }
  .title-banner p { margin: 0; }
  .title-banner .product-name { font-size: 32px; }
  .section { position: absolute; left: 65px; }
  .section h2 {
    margin: 0 0 6px;
    font-weight: 700;
    font-size: 21px;
    letter-spacing: 0.2px;
    color: var(--navy);
  }
  .section ul { list-style: none; margin: 0; padding: 0; font-size: 14.5px; }
  .features { top: 494px; }
  .features li { line-height: 19px; margin-bottom: 5.7px; }
  .features li .wrap { display: block; padding-left: 7px; }
  .options { top: 797px; }
  .options li { line-height: 24.5px; }
  .options b { font-weight: 600; color: var(--navy); }
  .use-cases { top: 1040px; color: var(--white); }
  .use-cases h2 { color: var(--white); margin-bottom: 10px; }
  .use-cases li { line-height: 24.5px; }
  .price {
    position: absolute;
    left: 531px; top: 826px;
    width: 300px;
    text-align: center;
    color: var(--white);
    font-weight: 700;
  }
  .price .label { font-size: 41px; line-height: 44px; display: block; }
  .price .amount { font-size: 59px; line-height: 64px; display: block; font-family: "Barlow Condensed", sans-serif; }
</style>
</head>
<body>
<div class="flyer">
  <svg class="flyer-art" width="927" height="1200" viewBox="0 0 927 1200">
    <defs>
      <linearGradient id="faintPhoto" x1="0" y1="0" x2="0" y2="1">
        <stop offset="0" stop-color="#e6ecf3"/>
        <stop offset="1" stop-color="#f3f4f6"/>
      </linearGradient>
      <linearGradient id="skyPhoto" x1="0" y1="0" x2="0" y2="1">
        <stop offset="0" stop-color="#6fa6e6"/>
        <stop offset="0.45" stop-color="#e9edf0"/>
        <stop offset="0.75" stop-color="#f6f7f8"/>
        <stop offset="1" stop-color="#3a3d42"/>
      </linearGradient>
      <linearGradient id="priceFill" x1="0" y1="0" x2="0" y2="1">
        <stop offset="0" stop-color="#5aa7f7"/>
        <stop offset="1" stop-color="#0d5cb5"/>
      </linearGradient>
    </defs>

    <rect class="backdrop" role="img" aria-label="Faint photo of the trailer house behind the text" x="0" y="0" width="927" height="1010" fill="url(#faintPhoto)"/>

    <g class="accent-strips" fill="#2e74d0">
      <polygon points="330,0 450,0 560,110 440,110"/>
      <polygon points="800,460 927,460 927,590 800,590" transform="rotate(0)" opacity="0"/>
      <polygon points="790,460 927,460 927,545 870,545"/>
    </g>

    <polygon class="title-band" points="0,337 357,337 484,467 0,467" fill="var(--banner)"/>

    <rect class="use-band" x="0" y="1010" width="927" height="190" fill="var(--band)"/>

    <g class="photo-diamond" role="img" aria-label="Side view of the white board-and-batten vending house">
      <rect x="171" y="-22" width="187" height="187" rx="26" transform="rotate(45 265 71)" fill="url(#skyPhoto)" stroke="var(--white)" stroke-width="9"/>
    </g>
    <g class="photo-diamond" role="img" aria-label="Front three-quarter view of the vending house on its tandem trailer">
      <rect x="423" y="-32" width="527" height="527" rx="50" transform="rotate(45 686 231)" fill="url(#skyPhoto)" stroke="var(--white)" stroke-width="10"/>
    </g>
    <g class="photo-diamond" role="img" aria-label="Vending house with the serving window open">
      <rect x="763" y="563" width="187" height="187" rx="26" transform="rotate(45 856 656)" fill="url(#skyPhoto)" stroke="var(--white)" stroke-width="9"/>
    </g>

    <rect class="price-diamond" x="551" y="748" width="260" height="260" rx="40" transform="rotate(45 681 878)" fill="url(#priceFill)" stroke="var(--white)" stroke-width="9"/>
  </svg>

  <div class="title-banner">
    <p>THE</p>
    <p class="product-name">“COTTAGE CREST MINI”</p>
    <p>LUXURY, MOBILE VENDING HOUSE</p>
  </div>

  <section class="section features">
    <h2>BASE UNIT FEATURES</h2>
    <ul>
      <li>-Trailer features tandem wheels with break</li>
      <li>-Steel frame construction for fire retardation<span class="wrap">safety and weight reduction.</span></li>
      <li>-100% off grid with solar and lithium battery<span class="wrap">system allowing the trailer to be used in</span><span class="wrap">places not accessible by the traditional trailers.</span></li>
      <li>-80 gallon water supply tank</li>
      <li>-100 gallon waste water tank</li>
      <li>-Cupboards, cabinets and four stainless steel sinks.</li>
      <li>-60” Gas shock serving window</li>
    </ul>
  </section>

  <section class="section options">
    <h2>AVAILABLE OPTIONS</h2>
    <ul>
      <li>-HVAC-Norvex Mini Split - <b>$8,000</b></li>
      <li>-Cooler - &nbsp;Glass fron Commercial refrigirator - <b>$1,600</b></li>
      <li>-Upper loft sotrage area - <b>$1,200</b></li>
      <li>-Sinage and Graphics - <b>$2,000 - $5,000</b> (depend on complexity)</li>
      <li>-Ice machine - <b>$1,100</b></li>
      <li>-Other custom items available on request</li>
    </ul>
  </section>

  <div class="price">
    <span class="label">BASE PRICE</span>
    <span class="amount">$45,000</span>
  </div>

  <section class="section use-cases">
    <h2>USE CASES</h2>
    <ul>
      <li>FOOD: Lemonade, Coffee, Pizza, Cookies, Doughnuts, Barbecue and more!</li>
      <li>RETAIL: Clothing, Watches, Jewelry, Flowers and more!</li>
      <li>CORPORATE: Product info, Demonstration, Information, Brand awareness.</li>
      <li>FUNDRAISERS: Girls/Boy sports, Non profits, etc.</li>
    </ul>
  </section>
</div>
</body>
</html>
```